Erstellung eines Polizeiwimpels für Kinder
Zielgruppe
Wir stellen Fahrradwimpel für Kinder her. Hier finden Sie unsere Produkte: https://www.kramladen.de/stores/node/58203916472
Aufgabenstellung
Wir möchten einen 'Polizeiwimpel' für Kinder herstellen.
Wenn möglich, nur eine Farbe verwenden (reduziert Kosten in der Produktion). Der Hintergrund soll 'Polizei Blau' sein.
Wimpelgröße: 17,5 cm X 32 cm X 32cm (Dreieckig)
Ich habe ein selbst erstelltes Design hochgeladen. Es soll den Schriftzug 'Polizei' enthalten und evtl. noch 'Polizei Symbole', die Jungs (und ihre Eltern) ansprechen. (Pistole, Sheriffstern, etc.) Das offizielle Wappen oder andere Hoheitssymbole dürfen wir allerdings nicht verwenden.

```html
<!DOCTYPE html>
<html lang="de">
<head>
<meta charset="utf-8">
<title>Polizeiwimpel</title>
<link rel="stylesheet" href="https://fonts.googleapis.com/css2?family=Roboto:wght@400;700&display=swap">
<style>
  :root {
    --pennant-blue: #043c80;
    --ink-white: #ffffff;
    --tint-blue: #8fa9cc;
    --page: #ffffff;
  }
  html, body {
    margin: 0;
    padding: 0;
    overflow: hidden;
    background: var(--page);
  }
  .canvas {
    width: 1200px;
    height: 848px;
    display: block;
  }
  .pennant-field { fill: var(--pennant-blue); }
  .pennant-title {
    font-family: "Roboto", Arial, sans-serif;
    font-weight: 700;
    font-size: 195px;
    fill: var(--ink-white);
  }
  .beacon-slot { fill: url(#beaconTone); }
  .pennant-url {
    font-family: "Roboto", Arial, sans-serif;
    font-weight: 400;
    font-size: 20px;
    fill: var(--ink-white);
  }
</style>
</head>
<body>
<svg class="canvas" viewBox="0 0 1200 848" xmlns="http://www.w3.org/2000/svg">
  <defs>
    <linearGradient id="beaconTone" x1="0" y1="0" x2="0" y2="1">
      <stop offset="0" stop-color="var(--tint-blue)"/>
      <stop offset="1" stop-color="var(--ink-white)"/>
    </linearGradient>
  </defs>

  <polygon class="pennant-field" points="64,101 1123,397 64,721"/>

  <g class="wordmark">
    <text class="pennant-title" x="114" y="470" textLength="106" lengthAdjust="spacingAndGlyphs">P</text>

    <rect class="beacon-slot" x="226" y="300" width="155" height="170" rx="6"
          role="img" aria-label="Blaulicht mit Lichtstrahlen anstelle des Buchstaben O"/>

    <text class="pennant-title" x="409" y="470" textLength="433" lengthAdjust="spacingAndGlyphs">LIZEI</text>
  </g>

  <text class="pennant-url" x="161" y="671" transform="rotate(-17.2 161 671)">www.radwimpel-werk.bike</text>
</svg>
</body>
</html>
```